Brill's Jewelers website (www.brillsjewelers-example.com)

We are in need of a web storefront for a retail Jewelry store.
www.brillsjewelers-example.com
https://www.facebook.com/Brills-Jewelers-Palm-Vista-740315928461257/

Brill's Jewelers is located in Coral Gables, Florida. The store has been family owned and operated since 1958. Their focus customers are high-income families that care about quality over the brand name. They mostly sell fashion jewelry and diamonds up to 8 carats. We are looking for a simple minimalistic site that their customers can view their inventory and purchase items online.

Competitors websites:
https://www.orvinjewelers-example.com/
http://www.pelvaro-example.com/
http://truecutjewelers-example.com/

Pages:
-Home (with message bulletin)
-Jewelry
We would be able to create the subpages ie Rings, Bracelets, Earrings, Necklaces, Estate, Watches, Men's, Children's
-Services
We would need sub pages ie Appraisals, Consignment, Repairs
-About us
-Contact

Target Market(s)

Local wealthy families

Coding

Number of Pages Required

Font styles to use
Serif

Requirements
Must have
• -An E-commerce site customers can buy jewelry online.
-An easy process internally to add new items to the site
-Colors are Black and White or Black and Gold
Nice to have
• I would like to stay away from face shots of random models in stock photos. I want the jewelry pieces as the focus, not models.

```html
<!DOCTYPE html>
<html lang="en">
<head>
<meta charset="utf-8">
<title>Brill's Jewelers</title>
<link href="https://fonts.googleapis.com/css2?family=Open+Sans:wght@300;400;600;800&display=swap" rel="stylesheet">
<style>
:root{
  --ink:#231f20;
  --ink-deep:#1c1a1b;
  --ink-card:#332e2f;
  --gold:#d4a93a;
  --paper:#ffffff;
  --mist:#f3f3f3;
  --text:#4a4a4a;
  --muted:#8a8a8a;
  --label:rgba(110,106,106,.85);
}
*{box-sizing:border-box;margin:0;padding:0}
html,body{width:1200px;height:2903px;overflow:hidden}
body{position:relative;background:var(--paper);font-family:'Open Sans',sans-serif;font-weight:300;color:var(--text)}
.abs{position:absolute}
a{color:inherit;text-decoration:none}

/* header */
.topbar{left:0;top:0;width:1200px;height:68px}
.topbar .phone{left:92px;top:11px;font-size:19px;color:#55565e}
.brand{left:0;width:1200px;top:6px;text-align:center;font-weight:800;font-size:44px;letter-spacing:2px;color:#111}
.util{right:80px;top:11px;font-size:12.5px;color:#7a7a8a;display:flex;gap:18px;align-items:center}
.nav{left:0;top:68px;width:1200px;height:41px;background:var(--ink);display:flex;justify-content:center;align-items:center;gap:0;font-size:13px;color:#fff;font-weight:400}
.nav a{padding:0 26px}
.nav .tag{color:var(--gold)}

/* hero */
.hero{left:9px;top:118px;width:1182px;height:400px;background:var(--mist)}
.hero h1{position:absolute;left:80px;width:335px;top:118px;text-align:center;font-weight:400;font-size:33px;color:#333}
.hero p{position:absolute;left:80px;width:335px;top:180px;text-align:center;font-size:13px;line-height:18px;color:#666}
.btn-gold{position:absolute;left:195px;top:242px;width:105px;height:37px;border:2px solid var(--gold);color:var(--gold);font-size:13px;display:flex;align-items:center;justify-content:center}
.hero .piece{position:absolute;left:690px;top:40px;width:400px;height:340px;border-radius:50%;background:radial-gradient(ellipse at 45% 45%,#ffffff 0%,#d8d8d8 45%,#b5b5b5 65%,rgba(243,243,243,0) 72%)}
.arrow{position:absolute}

/* shop */
.shop{left:0;top:527px;width:1200px;height:762px;background:var(--ink)}
.vline{position:absolute;top:0;width:1px;height:762px;background:#3b3637}
.sec-title{position:absolute;left:0;width:1200px;text-align:center;font-weight:400;font-size:37px}
.gold-rule{position:absolute;left:520px;width:160px;height:1px;background:var(--gold)}
.tile{position:absolute;background:#fff}
.tile .img{position:absolute;inset:0}
.tile .label{position:absolute;left:50%;top:50%;transform:translate(-50%,-50%);background:var(--label);color:#fff;font-size:17px;font-weight:400;padding:6px 20px;white-space:nowrap}

/* history */
.history{left:0;top:1289px;width:1200px;height:793px}
.collage{left:130px;top:210px;width:400px;height:518px;background:linear-gradient(135deg,#3a3a3a,#8d8578 50%,#2a2a2a)}
.story{left:559px;top:199px;width:535px;font-size:14.5px;line-height:22.6px;color:#555}
.story p{margin-bottom:18px}
.btn-outline{left:559px;top:599px;width:158px;height:41px;border:1px solid #333;color:#333;font-size:17px;font-weight:400;display:flex;align-items:center;justify-content:center}

/* clients */
.clients{left:0;top:2082px;width:1200px;height:483px;background:var(--ink);overflow:hidden}
.ghost{position:absolute;left:0;width:1200px;top:-10px;text-align:center;font-size:170px;font-weight:800;letter-spacing:6px;color:#2a2627}
.card{position:absolute;top:202px;width:301px;height:156px;background:var(--ink-card)}
.card .top{height:66px;border-bottom:1px solid #2a2627;position:relative}
.avatar{position:absolute;left:17px;top:18px;width:32px;height:32px;border-radius:50%;background:#e8e8e8}
.card .name{position:absolute;left:58px;top:17px;color:var(--gold);font-weight:600;font-size:13px}
.card .handle{position:absolute;left:58px;top:35px;color:#9a9a9a;font-size:11.5px}
.card .net{position:absolute;right:18px;top:20px;width:16px;height:16px;border-radius:50%;background:#6b6566}
.card .quote{padding:16px 17px;color:#ddd;font-size:12.5px;line-height:18px}
.dots{left:580px;top:2459px;display:flex;gap:8px}
.dots span{width:5px;height:5px;border-radius:50%;background:#4a4546}
.dots span:first-child{background:#ccc}

/* footer */
.footer{left:0;top:2565px;width:1200px;height:263px;background:var(--ink-deep);color:#ddd}
.flogo{left:146px;top:58px;width:218px;text-align:center}
.flogo .mark{font-weight:800;font-size:44px;letter-spacing:2px;color:#bfbfbf;line-height:50px}
.flogo .sub{border-top:1px solid #9a9a9a;font-size:14px;letter-spacing:1px;color:#9a9a9a;padding-top:2px}
.fcol{top:64px}
.fcol h3{font-weight:400;font-size:18px;color:#e8e8e8}
.fcol .rule{width:90px;height:1px;background:var(--gold);margin:14px 0 14px}
.fcol p{font-size:14.5px;line-height:23px;color:#e0e0e0}
.fcol .dir{color:var(--gold)}
.copy{left:0;top:2828px;width:1200px;height:75px;background:var(--ink-deep);border-top:1px solid #2a2627;text-align:center;line-height:75px;font-size:14.5px;color:#ccc}
</style>
</head>
<body>

<header class="abs topbar">
  <div class="abs phone">(305) 555-0148</div>
  <div class="abs brand">BRILL'S</div>
  <div class="abs util"><span>Wishlist</span><span>My account</span>
    <svg width="13" height="13" viewBox="0 0 13 13"><circle cx="5.5" cy="5.5" r="4" fill="none" stroke="#333" stroke-width="2"/><line x1="8.5" y1="8.5" x2="12" y2="12" stroke="#333" stroke-width="2"/></svg>
  </div>
</header>
<nav class="abs nav">
  <a>Home</a><a>Jewelry &#8964;</a><a>Services</a><a class="tag">YOUR HOMETOWN JEWELER SINCE 1958</a><a>Diamonds</a><a>About us</a><a>Contact</a>
</nav>

<section class="abs hero">
  <h1>New Collection</h1>
  <p>Lorem ipsum dolor sit amet consectetur adipiscing elit dolor</p>
  <a class="btn-gold">shop now</a>
  <div class="piece" role="img" aria-label="Diamond halo engagement ring with pavé band"></div>
  <svg class="arrow" style="left:23px;top:182px" width="24" height="38" viewBox="0 0 24 38"><polyline points="20,3 5,19 20,35" fill="none" stroke="#999" stroke-width="4"/></svg>
  <svg class="arrow" style="left:1136px;top:182px" width="24" height="38" viewBox="0 0 24 38"><polyline points="4,3 19,19 4,35" fill="none" stroke="#999" stroke-width="4"/></svg>
</section>

<section class="abs shop">
  <div class="vline" style="left:400px"></div>
  <div class="vline" style="left:799px"></div>
  <h2 class="sec-title" style="top:50px;color:#fff">Shop For Jewelry</h2>
  <div class="gold-rule" style="top:120px"></div>

  <div class="tile" style="left:200px;top:170px;width:351px;height:252px">
    <div class="img" role="img" aria-label="Gold diamond solitaire pendant necklace" style="background:radial-gradient(circle at 50% 55%,#eadfbf 0%,#fff 45%)"></div>
    <span class="label">Shop Necklaces</span>
  </div>
  <div class="tile" style="left:568px;top:170px;width:433px;height:252px">
    <div class="img" role="img" aria-label="Diamond halo ring" style="background:radial-gradient(ellipse at 50% 50%,#cfd2d4 0%,#fff 40%)"></div>
    <span class="label">Shop Rings</span>
  </div>
  <div class="tile" style="left:200px;top:440px;width:254px;height:251px">
    <div class="img" role="img" aria-label="Black and white diamond bracelet" style="background:radial-gradient(ellipse at 50% 45%,#d5d5d5 0%,#fff 50%)"></div>
    <span class="label">Shop Bracelets</span>
  </div>
  <div class="tile" style="left:472px;top:440px;width:256px;height:251px">
    <div class="img" role="img" aria-label="Pearl and diamond earrings" style="background:radial-gradient(ellipse at 50% 50%,#dcdcdc 0%,#fff 50%)"></div>
    <span class="label">Shop Earrings</span>
  </div>
  <div class="tile" style="left:746px;top:440px;width:253px;height:251px">
    <div class="img" role="img" aria-label="Diamond cross pendant on chain" style="background:radial-gradient(ellipse at 50% 50%,#dadada 0%,#fff 45%)"></div>
    <span class="label">Men's Jewelry</span>
  </div>
</section>

<section class="abs history">
  <h2 class="sec-title" style="top:47px;color:#444;font-size:32px;font-weight:300">Our History</h2>
  <div class="gold-rule" style="top:115px"></div>
  <div class="abs collage" role="img" aria-label="Collage of family photographs and the storefront"></div>
  <div class="abs story">
    <p>Harold and Mae Brill started their jewelry store in the center of Cedar Bay, FL with $600, a few display cases, a small safe, and the family dining room table as the main showcase. Harold Brill, Sr. attended Halden School of Watchmakers in New York and became a certified watchmaker in 1946. In 1961, he became a certified gemologist.</p>
    <p>In 1984, Brill's expanded and relocated their business to their current location in the heart of Palm Vista on Main Street. They were the first tenants to sign a lease in the town center.</p>
    <p>Brill's Jewelers is best known for their campaign that offered transportation in a “Brill White Silver Coach” to the couple who purchased their engagement ring from their store.</p>
    <p>Brill's Jewelers is still run today as a family owned and operated full-service jewelry store that combines a high-level expertise with a rich tradition in the Coastal County area.</p>
  </div>
  <a class="abs btn-outline">Read Full Story</a>
</section>

<section class="abs clients">
  <div class="ghost" aria-hidden="true">BRILL'S</div>
  <h2 class="sec-title" style="top:50px;color:#fff;font-size:32px">What Our Clients Think</h2>
  <div class="gold-rule" style="top:116px"></div>
  <svg class="arrow" style="left:117px;top:272px" width="14" height="22" viewBox="0 0 14 22"><polyline points="11,2 3,11 11,20" fill="none" stroke="#fff" stroke-width="3"/></svg>
  <svg class="arrow" style="left:1069px;top:272px" width="14" height="22" viewBox="0 0 14 22"><polyline points="3,2 11,11 3,20" fill="none" stroke="#fff" stroke-width="3"/></svg>

  <div class="card" style="left:135px">
    <div class="top"><span class="avatar"></span><span class="name">Marisol T.</span><span class="handle">@username</span><span class="net"></span></div>
    <p class="quote">Lorem ipsum dolor sit amet, consectetur adipiscing elit. Ut elit tellus, luctus nec ullamcorper mattis, pulvinar dapibus leo.</p>
  </div>
  <div class="card" style="left:450px">
    <div class="top"><span class="avatar"></span><span class="name">Renata D.</span><span class="handle">@username</span><span class="net"></span></div>
    <p class="quote">Lorem ipsum dolor sit amet, consectetur adipiscing elit. Ut elit tellus, luctus nec ullamcorper mattis, pulvinar dapibus leo.</p>
  </div>
  <div class="card" style="left:764px">
    <div class="top"><span class="avatar"></span><span class="name">Joanna P.</span><span class="handle">@username</span><span class="net"></span></div>
    <p class="quote">Lorem ipsum dolor sit amet, consectetur adipiscing elit. Ut elit tellus, luctus nec ullamcorper mattis, pulvinar dapibus leo.</p>
  </div>
</section>
<div class="abs dots"><span></span><span></span><span></span></div>

<footer class="abs footer">
  <div class="abs flogo"><div class="mark">BRILL'S</div><div class="sub">YOUR HOMETOWN JEWELER</div></div>
  <div class="abs fcol" style="left:449px">
    <h3>Our Location</h3><div class="rule"></div>
    <p>(305) 555-0148</p>
    <p style="margin-top:18px">412 Harbor Lane | Palm Vista, FL 33099</p>
    <p class="dir">Get Directions</p>
  </div>
  <div class="abs fcol" style="left:796px">
    <h3>Our Store Hours</h3><div class="rule"></div>
    <p>Tuesday – Friday: 10:30am – 6:30pm<br>Saturday: 10:30am – 5:30pm<br>Holiday Hours May Vary</p>
  </div>
</footer>
<div class="abs copy">© 2020 Brill's Jewelers. All Rights Reserved.</div>

</body>
</html>
```